Website upgrade

I have two websites linked to the same business. One is for commercial and retail clients the other is for private and residential customers. I need a creative, modern thinking and bold designer to redesign my sites so that they look more professional and eye catching. The two sites are: www.marcusfieldingltd.com and www.pkrfittingservices.com

Target Market(s)

pkr fittings targets home owners and individuals who want work done to their property and marcus fielding targets commercial customers who want shopfitting work undertaken

Industry/Entity Type

Home Improvement

Number of Pages Required

5+ page

Font styles to use
Sans Serif

Colors
0255a3
3176b5
0292cd
85acd3
85cae6

Requirements
Must have
• i want a site to reflect my existing sites but with a bit more of a wow factor to draw customers in
Nice to have
• logo designed, video or slide show
Should not have
• blog page

```html
<!DOCTYPE html>
<html lang="en">
<head>
<meta charset="utf-8">
<title>Marcus Fielding Contracting Ltd</title>
<link href="https://fonts.googleapis.com/css2?family=Alegreya:wght@400;500&family=Alegreya+SC&family=Open+Sans:wght@300;400;600;700&display=swap" rel="stylesheet">
<style>
:root{
  --sky-top:#a9c3e6;
  --sky-bottom:#8eb0dd;
  --nav-active:#4a5f80;
  --ink:#2b2b2b;
  --muted:#8a8a8a;
  --body:#555;
  --panel:#efefef;
  --white:#ffffff;
  --button:#94b4e0;
  --band-top:#0255a3;
  --band-bottom:#0a2457;
  --client:#6f6f6f;
  --serif:'Alegreya', Georgia, serif;
  --sans:'Open Sans', Arial, sans-serif;
}
*{margin:0;padding:0;box-sizing:border-box}
html,body{width:1200px;height:2612px;overflow:hidden}
body{font-family:var(--sans);color:var(--ink);background:var(--white);position:relative}
section,header,footer{position:absolute;left:0;width:1200px}

.site-header{top:0;height:175px;background:linear-gradient(180deg,var(--sky-top),var(--sky-bottom));border-bottom:3px solid #5a6f90}
.brand{position:absolute;left:145px;top:38px;display:flex;align-items:center;gap:14px}
.brand-mark{width:58px;height:58px;border-radius:50%;background:#1c2330}
.brand-name{font-family:var(--serif);font-size:25px;letter-spacing:.5px;color:#111}
.main-nav{position:absolute;left:145px;top:125px;display:flex;height:50px}
.main-nav a{display:block;height:50px;line-height:52px;padding:0 22px;margin-right:14px;font-family:var(--serif);font-size:17px;color:#1d2533;text-decoration:none;text-transform:uppercase}
.main-nav a.is-active{background:var(--nav-active);color:#fff;border-radius:4px 4px 0 0}

.hero{top:175px;height:511px;overflow:hidden}
.hero-photo{position:absolute;inset:0;background:
  radial-gradient(ellipse 300px 220px at 1060px 170px,rgba(255,255,255,.75),rgba(255,255,255,0) 70%),
  radial-gradient(ellipse 260px 300px at 360px 200px,rgba(230,180,110,.55),rgba(230,180,110,0) 70%),
  radial-gradient(ellipse 520px 160px at 560px 480px,rgba(40,30,24,.75),rgba(40,30,24,0) 75%),
  radial-gradient(ellipse 200px 140px at 880px 230px,rgba(200,205,210,.7),rgba(200,205,210,0) 70%),
  linear-gradient(180deg,#e9e7e3 0%,#c8bfb1 35%,#8d7b66 62%,#4b3d31 85%,#2e2620 100%)}
.hero-title{position:absolute;top:290px;width:100%;text-align:center;font-family:'Alegreya SC',Georgia,serif;font-weight:400;font-size:38px;color:#fff;letter-spacing:1px;text-shadow:0 1px 3px rgba(0,0,0,.35)}
.hero-dots{position:absolute;top:455px;left:568px;display:flex;gap:7px}
.hero-dots span{width:8px;height:8px;border-radius:50%;background:rgba(255,255,255,.55)}
.hero-dots span.is-active{background:#fff}

.welcome{top:686px;height:352px;background:var(--panel);text-align:center}
.section-title{font-family:var(--serif);font-size:25px;font-weight:400;color:var(--ink);text-transform:uppercase;letter-spacing:.5px}
.welcome .section-title{margin-top:58px}
.welcome-text{width:910px;margin:22px auto 0;font-size:12.5px;line-height:24px;color:var(--body)}
.btn-contact{display:inline-block;margin-top:44px;width:185px;height:42px;line-height:42px;background:var(--button);color:#fff;font-family:var(--serif);font-size:14px;border-radius:4px;text-decoration:none;text-transform:uppercase}

.services{top:1038px;height:518px;background:var(--white)}
.services .section-title{position:absolute;top:48px;width:100%;text-align:center}
.service{position:absolute;top:117px;width:287px}
.service-photo{height:237px}
.service-name{margin-top:24px;font-family:var(--serif);font-size:26px;font-weight:400;text-transform:uppercase;color:var(--ink)}
.service-name small{font-size:11px}
.service-desc{margin-top:6px;font-size:12.5px;color:var(--muted)}

.gallery{top:1556px;height:468px;background:var(--panel)}
.gallery .section-title{position:absolute;top:55px;width:100%;text-align:center}
.gallery-main{position:absolute;left:145px;top:134px;width:442px;height:271px;overflow:hidden;box-shadow:0 6px 12px rgba(0,0,0,.2);background:
  radial-gradient(ellipse 180px 60px at 230px 95px,rgba(170,140,100,.85),rgba(170,140,100,0) 75%),
  radial-gradient(ellipse 240px 70px at 200px 200px,rgba(215,205,170,.7),rgba(215,205,170,0) 75%),
  linear-gradient(180deg,#2f4a26 0%,#4e6a36 30%,#6f7f4a 55%,#7d8a52 75%,#4f6a30 100%)}
.gallery-caption{position:absolute;left:0;bottom:0;width:100%;height:48px;line-height:48px;padding-left:12px;background:rgba(0,0,0,.55);color:#fff;font-size:13px}
.gallery-arrow{position:absolute;top:100px;width:40px;height:42px;background:#8fb0dc;display:flex;align-items:center;justify-content:center}
.gallery-thumb{position:absolute;width:209px;height:123px;box-shadow:0 6px 12px rgba(0,0,0,.2)}

.contact-band{top:2024px;height:249px;background:linear-gradient(180deg,var(--band-top),var(--band-bottom));color:#fff;text-align:center}
.contact-lead{width:860px;margin:40px auto 0;font-size:19px;line-height:30px;font-weight:300;color:#e8eef8}
.contact-line{display:flex;justify-content:center;align-items:center;gap:14px;font-size:22px;font-weight:300;color:#fff}
.contact-phone{margin-top:30px}
.contact-mail{margin-top:14px}

.clients{top:2273px;height:199px;background:var(--white)}
.clients .section-title{position:absolute;top:42px;width:100%;text-align:center}
.client-row{position:absolute;top:110px;left:165px;width:870px;display:flex;justify-content:space-between;align-items:center}
.client{display:flex;align-items:center;gap:8px;font-family:var(--sans);font-weight:700;font-size:26px;color:var(--client)}
.client-dot{width:14px;height:14px;border-radius:50%;background:var(--client)}
.client-arrow{position:absolute;top:114px}

.site-footer{top:2472px;height:140px;background:var(--panel);text-align:center}
.footer-nav{margin-top:44px;font-family:var(--serif);font-size:13px;color:#333;text-transform:uppercase}
.footer-nav span{margin:0 14px;color:#666}
.copyright{margin-top:16px;font-family:var(--serif);font-size:12.5px;color:#333}
</style>
</head>
<body>

<header class="site-header">
  <div class="brand">
    <div class="brand-mark" role="img" aria-label="Company emblem"></div>
    <div class="brand-name">MARCUS FIELDING CONTRACTING LTD</div>
  </div>
  <nav class="main-nav">
    <a class="is-active" href="#">Home</a>
    <a href="#">About</a>
    <a href="#">Services</a>
    <a href="#">Testimonials</a>
    <a href="#">Quotes &amp; Estimates</a>
    <a href="#">Contact</a>
  </nav>
</header>

<section class="hero">
  <div class="hero-photo" role="img" aria-label="Modern fitted kitchen with pendant lights, island worktop and steel appliances"></div>
  <h1 class="hero-title">Marcus Fielding Contracting</h1>
  <div class="hero-dots"><span class="is-active"></span><span class="is-active"></span><span></span><span></span></div>
</section>

<section class="welcome">
  <h2 class="section-title">Welcome to Marcus Fielding Contracting Ltd</h2>
  <p class="welcome-text">With over 25 years experience, PKR Fitting Services provide high-quality Joinery, carpentry &amp; property services throughout the Huddersfield area. Our primary trades are Joinery &amp; Carpentry, but we also specialise in Kitchen installation, Bathroom Installation, small building works and property refurbishments. We also undertake property maintenance and carryout a vast range of jobs around the home. Whether you are a home owner looking for minor repairs or a landlord in need of property care and maintenance, PKR Fitting Services are here to help.</p>
  <a class="btn-contact" href="#">Contact us</a>
</section>

<section class="services">
  <h2 class="section-title">Our Services</h2>
  <div class="service" style="left:145px">
    <div class="service-photo" role="img" aria-label="Modern house shown half as architectural line drawing" style="background:radial-gradient(ellipse 160px 90px at 230px 200px,rgba(60,110,180,.75),rgba(60,110,180,0) 75%),radial-gradient(ellipse 140px 120px at 60px 60px,rgba(255,255,255,.9),rgba(255,255,255,0) 75%),linear-gradient(135deg,#f6f8fb 0%,#dde6f1 45%,#9fb6d6 75%,#4f6e9e 100%)"></div>
    <h3 class="service-name">Property Services</h3>
    <p class="service-desc">Refurbishment, Maintenance &amp; Repairs</p>
  </div>
  <div class="service" style="left:456px">
    <div class="service-photo" role="img" aria-label="Construction crane with hard hat and plans on a desk" style="background:radial-gradient(ellipse 70px 45px at 170px 150px,rgba(240,190,40,.85),rgba(240,190,40,0) 75%),radial-gradient(ellipse 200px 60px at 143px 215px,rgba(110,95,75,.8),rgba(110,95,75,0) 80%),linear-gradient(180deg,#6fb0c6 0%,#9cc7cf 45%,#b8cfcd 65%,#8a7a62 100%)"></div>
    <h3 class="service-name">Site Services</h3>
    <p class="service-desc">Project &amp; Site Management</p>
  </div>
  <div class="service" style="left:768px">
    <div class="service-photo" role="img" aria-label="Shop interior with fitted partitions and display rails" style="background:radial-gradient(ellipse 30px 70px at 260px 110px,rgba(170,40,40,.7),rgba(170,40,40,0) 80%),linear-gradient(90deg,#7e7b77 0%,#d9d6d1 22%,#f0eee9 40%,#8e8a85 52%,#e6e3de 62%,#f2f0ec 80%,#9a9692 100%)"></div>
    <h3 class="service-name">Contracting <small>(Sub-Contracting)</small></h3>
    <p class="service-desc">Shopfitting &amp; Installation Services</p>
  </div>
</section>

<section class="gallery">
  <h2 class="section-title">Photo Gallery</h2>
  <div class="gallery-main" role="img" aria-label="Landscaped garden with timber decking and seating">
    <div class="gallery-arrow" style="left:0">
      <svg width="12" height="14" viewBox="0 0 12 14"><path d="M8 2 L3 7 L8 12" stroke="#fff" stroke-width="2" fill="none"/></svg>
    </div>
    <div class="gallery-arrow" style="right:0">
      <svg width="12" height="14" viewBox="0 0 12 14"><path d="M4 2 L9 7 L4 12" stroke="#fff" stroke-width="2" fill="none"/></svg>
    </div>
    <div class="gallery-caption">Neque porro quisquam est qui dolorem ipsum quia dolor ......</div>
  </div>
  <div class="gallery-thumb" role="img" aria-label="White fitted kitchen" style="left:611px;top:134px;background:radial-gradient(ellipse 90px 30px at 110px 58px,rgba(40,40,40,.7),rgba(40,40,40,0) 80%),linear-gradient(180deg,#f2f1ee 0%,#dedbd6 40%,#b9b4ac 70%,#6a655f 100%)"></div>
  <div class="gallery-thumb" role="img" aria-label="Kitchen with wooden worktops" style="left:845px;top:134px;background:radial-gradient(ellipse 80px 40px at 150px 40px,rgba(250,230,180,.8),rgba(250,230,180,0) 75%),linear-gradient(180deg,#9a6230 0%,#c9904e 40%,#e0c28e 65%,#a8743c 100%)"></div>
  <div class="gallery-thumb" role="img" aria-label="Beige kitchen units with built-in oven" style="left:611px;top:282px;background:radial-gradient(ellipse 30px 30px at 90px 75px,rgba(50,40,35,.7),rgba(50,40,35,0) 80%),linear-gradient(180deg,#8e7a64 0%,#c7a886 30%,#dcc6a4 60%,#a88c6a 100%)"></div>
  <div class="gallery-thumb" role="img" aria-label="Brick conservatory extension" style="left:845px;top:282px;background:radial-gradient(ellipse 60px 50px at 130px 70px,rgba(240,240,240,.85),rgba(240,240,240,0) 80%),linear-gradient(90deg,#8a4a36 0%,#a35c44 40%,#c7c9cc 60%,#d8dadc 100%)"></div>
</section>

<section class="contact-band">
  <p class="contact-lead">Our main website is currently undergoing an overhaul, so if you require any further information, or would like to book a consultation please do not hesitate to contact us on</p>
  <div class="contact-line contact-phone">
    <svg width="20" height="20" viewBox="0 0 24 24"><path fill="#fff" d="M6.6 10.8a15.1 15.1 0 0 0 6.6 6.6l2.2-2.2a1 1 0 0 1 1-.25 11.4 11.4 0 0 0 3.6.57 1 1 0 0 1 1 1V20a1 1 0 0 1-1 1A17 17 0 0 1 3 4a1 1 0 0 1 1-1h3.5a1 1 0 0 1 1 1c0 1.25.2 2.45.57 3.57a1 1 0 0 1-.25 1z"/></svg>
    <span>|</span><span>07700 900318</span>
  </div>
  <div class="contact-line contact-mail">
    <svg width="22" height="18" viewBox="0 0 22 18"><rect x="1" y="1" width="20" height="16" rx="2" fill="none" stroke="#fff" stroke-width="2"/><path d="M2 3 L11 10 L20 3" fill="none" stroke="#fff" stroke-width="2"/></svg>
    <span>|</span><span>sales@marcusfieldingltd.com, sales@pkrfittingservices.com</span>
  </div>
</section>

<section class="clients">
  <h2 class="section-title">Clients</h2>
  <svg class="client-arrow" style="left:80px" width="12" height="18" viewBox="0 0 12 18"><path d="M9 2 L3 9 L9 16" stroke="#aaa" stroke-width="2" fill="none"/></svg>
  <div class="client-row">
    <div class="client"><span class="client-dot"></span>Harlow Motors</div>
    <div class="client">Fresco Deli</div>
    <div class="client">Bite.</div>
    <div class="client">Greenway's</div>
    <div class="client">Valemart</div>
  </div>
  <svg class="client-arrow" style="left:1108px" width="12" height="18" viewBox="0 0 12 18"><path d="M3 2 L9 9 L3 16" stroke="#aaa" stroke-width="2" fill="none"/></svg>
</section>

<footer class="site-footer">
  <div class="footer-nav">Home<span>|</span>About<span>|</span>Services<span>|</span>Testimonials<span>|</span>Quotes &amp; Estimates<span>|</span>Contact</div>
  <p class="copyright">© 2016 COMPANY NAME &nbsp;| ALL RIGHTS RESERVED</p>
</footer>

</body>
</html>
```